MOV Promotional flyer for students

We're looking for an 8.5" x 11" flyer that will be distributed to schools. Please see language to include in attached files.

Target Market(s)

The parents and teachers of high school students

Industry/Entity Type

Mental health

Other font styles liked:
• Monserrat and Roboto Slab

Requirements
Must have
• See attached pdf for language to be included on the flyer. Please use the color palette from our website: www.lumemov.tv. Please include some imagery of students. Please ensure the
Nice to have
• Feel free to use any of the graphics provided. See our website for our brand look & feel: www.lumemov.tv

```html
<!DOCTYPE html>
<html lang="en">
<head>
<meta charset="utf-8">
<title>MOV Fundraising Flyer</title>
<link rel="stylesheet" href="https://fonts.googleapis.com/css2?family=Montserrat:wght@400;500;700;800&display=swap">
<style>
  :root {
    --navy: #24304a;
    --orange: #f07f2a;
    --teal: #5b8ea6;
    --sky: #9bbdd0;
    --peach: #f7c9aa;
    --ink: #4a4f5a;
    --paper: #ffffff;
    --stage: #ececec;
  }
  * { margin: 0; padding: 0; box-sizing: border-box; }
  html, body { width: 1200px; height: 3020px; overflow: hidden; }
  body { background: var(--stage); font-family: "Montserrat", Arial, sans-serif; position: relative; }

  .flyer {
    position: absolute; left: 50px; top: 798px;
    width: 1100px; height: 1424px;
    background: var(--paper); overflow: hidden;
  }
  .decor { position: absolute; left: 0; top: 0; width: 1100px; height: 1424px; }

  .brand { position: absolute; left: 40px; top: 84px; display: flex; align-items: center; gap: 16px; }
  .brand-dot { width: 64px; height: 64px; border-radius: 50%; background: var(--orange); }
  .brand-name { font-weight: 800; font-size: 52px; color: var(--orange); letter-spacing: 1px; }

  .headline {
    position: absolute; left: 40px; top: 246px;
    font-weight: 800; font-size: 54px; line-height: 66px; color: var(--navy);
  }
  .stat {
    position: absolute; left: 34px; top: 430px;
    font-weight: 800; font-size: 160px; line-height: 170px; color: var(--orange); letter-spacing: -4px;
  }
  .stat-note {
    position: absolute; left: 40px; top: 612px;
    font-weight: 800; font-size: 30px; line-height: 40px; color: var(--orange);
  }

  .photo { position: absolute; }
  .photo-expert {
    left: 478px; top: 126px; width: 588px; height: 572px;
    background: linear-gradient(160deg, #8c7a6a 0%, #b39a87 45%, #d9c6b5 100%);
  }
  .expert-label {
    position: absolute; left: 555px; top: 630px; width: 511px; height: 70px;
    background: var(--orange); color: var(--paper);
    font-weight: 700; font-size: 40px; line-height: 70px; padding-left: 26px;
  }
  .photo-students {
    left: 40px; top: 786px; width: 452px; height: 384px;
    background: linear-gradient(135deg, #e4e0dc 0%, #9b8f86 50%, #3c3a3c 100%);
  }

  .support {
    position: absolute; left: 530px; top: 790px;
    font-weight: 800; font-size: 44px; line-height: 50px; color: var(--navy);
  }
  .support .accent { display: block; color: var(--teal); }
  .support-body {
    position: absolute; left: 556px; top: 964px; width: 500px;
    border-left: 4px solid var(--orange); padding-left: 26px;
    font-weight: 500; font-size: 25px; line-height: 34px; color: var(--ink);
  }

  .web-pill {
    position: absolute; left: 322px; top: 1334px; width: 404px; height: 50px;
    border-radius: 25px; background: var(--orange); color: var(--paper);
    font-weight: 500; font-size: 26px; line-height: 50px; text-align: center; letter-spacing: 1px;
  }
</style>
</head>
<body>
  <main class="flyer">
    <svg class="decor" viewBox="0 0 1100 1424" aria-hidden="true">
      <circle cx="1010" cy="-10" r="120" fill="var(--navy)"/>
      <circle cx="800" cy="40" r="90" fill="var(--sky)"/>
      <rect x="1000" y="70" width="100" height="140" fill="var(--orange)"/>
      <path d="M1100 60 Q1040 110 1100 170 Z" fill="var(--teal)"/>
      <circle cx="60" cy="1400" r="190" fill="var(--teal)"/>
      <circle cx="220" cy="1430" r="70" fill="var(--sky)"/>
      <path d="M1100 1160 L1100 1424 L840 1424 Z" fill="var(--peach)"/>
    </svg>

    <div class="brand">
      <span class="brand-dot"></span>
      <span class="brand-name">MOV</span>
    </div>

    <h1 class="headline">FUNDRAISE<br>WITH MOV</h1>
    <p class="stat">50%</p>
    <p class="stat-note">OF ALL PROCEEDS GO<br>BACK TO YOUR SCHOOL</p>

    <div class="photo photo-expert" role="img" aria-label="Portrait photo of a smiling clinician with glasses in an office"></div>
    <p class="expert-label">Dr Vellaro, PSYD</p>

    <div class="photo photo-students" role="img" aria-label="Photo of two students in hats working together on a laptop"></div>

    <h2 class="support">SUPPORT THE<br>MENTAL HEALTH<span class="accent">OF YOUR STUDENTS</span></h2>
    <p class="support-body">MOV is a simple and effective way to improve mental health. Your students will learn valuable coping skills and techniques from expert clinicians who analyze real cases and share their insights and advice.</p>

    <p class="web-pill">WWW.LUMEMOV.TV</p>
  </main>
</body>
</html>
```